Website for Torvane Capital - investment banking firm

We have a corporate identity (thanks to Ravella/48213) and want to extend that into a website design.  See the attached zipped files.
We have software folks in-house to do the coding.
See the attached Project Brief & Notes for more details.  Don't worry about the actual text - lorem ipsum will be fine.
The server will be Apache.
Thank you!
Leopold

```html
<!DOCTYPE html>
<html lang="en">
<head>
<meta charset="utf-8">
<title>Torvane Capital</title>
<link rel="stylesheet" href="https://fonts.googleapis.com/css2?family=Cinzel:wght@400;500&family=Libre+Baskerville&family=Nunito+Sans:ital,wght@0,300;0,400;0,600;0,700;1,400&display=swap">
<style>
:root{
  --brand:#0a5bb0;
  --brand-dark:#003f80;
  --nav-text:#9cc3ea;
  --ink:#4a4f58;
  --muted:#6b7280;
  --footer-bg:#e3e8f1;
  --white:#ffffff;
  --headline:#0c4f9e;
}
*{margin:0;padding:0;box-sizing:border-box}
html,body{width:1145px;height:1200px;overflow:hidden}
body{position:relative;background:#fbfcfe;font-family:"Nunito Sans",sans-serif;color:var(--ink)}
.abs{position:absolute}

.site-header{left:0;top:0;width:1145px;height:78px;background:#fafbfc}
.brand{display:flex;align-items:center;gap:12px;white-space:nowrap}
.brand-mark{flex:none;width:40px;height:40px;background:var(--brand)}
.brand-name{font-family:"Nunito Sans",sans-serif;font-weight:600;color:var(--brand);letter-spacing:1px}
.site-header .brand{left:154px;top:19px}
.site-header .brand-name{font-size:24px}

.main-nav{left:0;top:78px;width:1145px;height:52px;background:var(--brand)}
.main-nav a{position:absolute;top:18px;font-size:13.5px;color:var(--nav-text);text-decoration:none;text-transform:uppercase;letter-spacing:.2px}
.main-nav a.active{color:var(--white);font-weight:700}

.hero{left:143px;top:130px;width:859px;height:457px;overflow:hidden}
.hero-photo{position:absolute;inset:0;background:linear-gradient(90deg,#4d5662 0%,#6f7d8c 30%,#a9c6e4 55%,#cfe0f1 75%,#b9d0e8 100%)}
.hero-photo::after{content:"";position:absolute;inset:0;background:linear-gradient(180deg,rgba(220,235,250,.25),rgba(120,150,190,.2))}
.hero-title{left:440px;top:78px;font-family:"Cinzel",serif;font-size:44px;line-height:51px;color:var(--headline);font-weight:500}
.hero-text{left:443px;top:252px;width:380px;font-size:15.5px;font-weight:300;line-height:21px;color:#4b5563}
.hero-dots{left:785px;top:367px;display:flex;gap:8px}
.hero-dots span{width:10px;height:10px;border-radius:50%;background:#8f9aae}
.hero-dots span.on{background:#4b1366;box-shadow:0 0 0 2px #fff}
.slide-arrow{top:275px;width:49px;height:53px;background:#b9bdc3}
.slide-arrow svg{position:absolute;left:17px;top:19px}

.feature{top:587px;width:286px;height:267px;color:var(--white)}
.feature h2{position:absolute;top:35px;font-family:"Libre Baskerville",serif;font-weight:400;font-size:19.5px}
.feature p,.feature ul{position:absolute;top:86px;font-size:11px;line-height:16px}
.feature ul{list-style:none}
.feature li{line-height:22.5px;padding-left:9px;position:relative}
.feature li::before{content:"";position:absolute;left:0;top:7px;border-left:4px solid #fff;border-top:4px solid transparent;border-bottom:4px solid transparent}
.feature .list-head{font-weight:700;text-transform:uppercase;padding-left:0}
.feature .list-head::before{display:none}
.btn-more{position:absolute;top:209px;width:71px;height:30px;border-radius:15px;background:linear-gradient(#fff,#e8eaee);color:#666;font-size:10px;text-align:center;line-height:30px;box-shadow:0 1px 2px rgba(0,0,0,.3)}
.feature-who{left:143px;background:linear-gradient(180deg,#0a57ab,#013d7e)}
.feature-services{left:429px;background:linear-gradient(180deg,#0866c8,#044c98)}
.feature-clients{left:715px;background:linear-gradient(180deg,#4a93de,#2c64a2)}

.site-footer{left:0;top:940px;width:1145px;height:218px;background:var(--footer-bg)}
.footer-brand{left:143px;top:33px;gap:9px}
.footer-brand .brand-mark{width:28px;height:28px}
.footer-brand .brand-name{font-size:15px;letter-spacing:.5px}
.footer-about{left:148px;top:91px;width:200px;font-size:11px;line-height:18px;color:#5b6170}
.footer-head{top:41px;font-size:11.5px;font-weight:700;letter-spacing:.6px;color:#4b5563;text-transform:uppercase}
.post{left:373px;display:flex;gap:13px}
.post-thumb{flex:none;width:48px;height:48px;background:linear-gradient(135deg,#4d5a66,#9aa9b8)}
.post-text{font-size:11px;line-height:18px;color:#5b6170;width:135px}
.post-text em{display:block;font-size:10px;color:#8a909c}
.newsletter-text{left:600px;top:69px;width:215px;font-size:11px;line-height:20px;color:#5b6170}
.subscribe{left:599px;top:117px;display:flex}
.subscribe .field{width:146px;height:33px;background:#a0aabd;color:#fff;font-size:11px;line-height:33px;padding-left:13px}
.subscribe .go{width:79px;height:33px;background:#3f4d66;color:#fff;font-size:12px;line-height:33px;text-align:center}
.contact-row{left:845px;display:flex;gap:12px;font-size:11px;line-height:18px;color:#5b6170}
.contact-row svg{flex:none;margin-top:2px}

.footer-bar{left:0;top:1158px;width:1145px;height:42px;background:var(--brand);color:#dce8f6;font-size:11px}
.footer-bar span{position:absolute;top:14px}
</style>
</head>
<body>

<header class="site-header abs">
  <div class="brand abs"><span class="brand-mark"></span><span class="brand-name">TORVANE CAPITAL</span></div>
</header>

<nav class="main-nav abs">
  <a class="active" style="left:182px">Home</a>
  <a style="left:258px">History</a>
  <a style="left:350px">Clients</a>
  <a style="left:437px">Our Team</a>
  <a style="left:541px">Completed Deals</a>
  <a style="left:702px">Current Searches</a>
  <a style="left:877px">Contact Us</a>
</nav>

<div class="slide-arrow abs" style="left:0"><svg width="12" height="16" viewBox="0 0 12 16"><path d="M9 1 L3 8 L9 15" stroke="#fff" stroke-width="2.5" fill="none"/></svg></div>
<div class="slide-arrow abs" style="left:1096px"><svg width="12" height="16" viewBox="0 0 12 16"><path d="M3 1 L9 8 L3 15" stroke="#fff" stroke-width="2.5" fill="none"/></svg></div>

<section class="hero abs">
  <div class="hero-photo" role="img" aria-label="Photo of a smiling businessman in a suit in a bright office, colleagues blurred in the background"></div>
  <h1 class="hero-title abs">Global,<br>Professional,<br>Trusted.</h1>
  <p class="hero-text abs">Torvane Capital is an independent investment bank working for buyers in a number of industries.</p>
  <div class="hero-dots abs"><span></span><span class="on"></span><span></span><span></span></div>
</section>

<section class="feature feature-who abs">
  <h2 style="left:30px">Who We Are</h2>
  <p style="left:30px;width:235px">Torvane Capital is an independent investment bank working for buyers in a number of industries. We utilize exceptional technology in finding companies to meet our client's search criteria. We will not waste a buyer's time, a seller's time, or our own time.</p>
  <span class="btn-more" style="left:37px">Read More</span>
</section>

<section class="feature feature-services abs">
  <h2 style="left:25px">Our Services</h2>
  <ul style="left:26px;top:84px">
    <li class="list-head">Our services include::</li>
    <li>Buy-Side Acquisitions</li>
    <li>Recapitalizations &amp; Growth Capital Partnerships</li>
    <li>Sell-Side Transactions</li>
  </ul>
  <span class="btn-more" style="left:37px">Read More</span>
</section>

<section class="feature feature-clients abs">
  <h2 style="left:27px">Our Clients</h2>
  <p style="left:27px;width:235px">Torvane Capital has a diverse array of clients ranging from multi-billion dollar strategic acquirers to large private equity funds. We will not engage a client as a buyer if we believe there is any chance of them wasting our time or a prospective seller's time.</p>
  <span class="btn-more" style="left:38px">Read More</span>
</section>

<footer class="site-footer abs">
  <div class="brand footer-brand abs"><span class="brand-mark"></span><span class="brand-name">TORVANE CAPITAL</span></div>
  <p class="footer-about abs">Donec volutpat, mi vel egestas eleif-end, dolor arcu iaculis nunc. Fusce gravida tortor felis, ac dictum risus<br><br>sagittis id. Morbi posuere justo eleif-end libero ultricies ultrices.</p>

  <h3 class="footer-head abs" style="left:372px">Recent Post</h3>
  <div class="post abs" style="top:68px">
    <div class="post-thumb" role="img" aria-label="Thumbnail photo of two business people"></div>
    <p class="post-text">Fusce gravida tortor felis, ac dictum risus sagittis<em>October 15, 2013</em></p>
  </div>
  <div class="post abs" style="top:138px">
    <div class="post-thumb" role="img" aria-label="Thumbnail photo of hands holding a tablet"></div>
    <p class="post-text">Fusce gravida tortor felis, ac dictum risus sagittis<em>October 15, 2013</em></p>
  </div>

  <h3 class="footer-head abs" style="left:600px;top:40px">Newsletter</h3>
  <p class="newsletter-text abs">Ipsum dolor sit amet, teft consecte tur adipiscing elit ut eunt.</p>
  <div class="subscribe abs"><span class="field">Email Address</span><span class="go">Subscribe</span></div>

  <h3 class="footer-head abs" style="left:843px">Contact Details</h3>
  <div class="contact-row abs" style="top:66px">
    <svg width="15" height="15" viewBox="0 0 24 24"><path d="M6.6 10.8a15 15 0 0 0 6.6 6.6l2.2-2.2a1 1 0 0 1 1-.25 11.4 11.4 0 0 0 3.6.57 1 1 0 0 1 1 1V20a1 1 0 0 1-1 1A17 17 0 0 1 3 4a1 1 0 0 1 1-1h3.5a1 1 0 0 1 1 1c0 1.25.2 2.45.57 3.570a1 1 0 0 1-.25 1z" fill="#737b88"/></svg>
    <span>+1800-555-0148</span>
  </div>
  <div class="contact-row abs" style="top:93px">
    <svg width="15" height="13" viewBox="0 0 16 13"><rect x="1" y="1" width="14" height="11" fill="none" stroke="#737b88" stroke-width="1.4"/><path d="M1 1 L8 7 L15 1" fill="none" stroke="#737b88" stroke-width="1.4"/></svg>
    <span>info@torvane-mail.com</span>
  </div>
  <div class="contact-row abs" style="top:120px">
    <svg width="15" height="17" viewBox="0 0 14 18"><path d="M7 0a6 6 0 0 0-6 6c0 4.5 6 12 6 12s6-7.5 6-12a6 6 0 0 0-6-6zm0 8.5A2.5 2.5 0 1 1 7 3.5a2.5 2.5 0 0 1 0 5z" fill="#737b88"/></svg>
    <span>Your Address, Your Country<br>Your Zip Code</span>
  </div>
</footer>

<div class="footer-bar abs">
  <span style="left:148px">Copyright © 2014 - TorvaneCapital. All Rights reserved</span>
  <span style="left:871px">Privacy Policy</span>
  <span style="left:980px">Sitemap</span>
</div>

</body>
</html>
```